Intenational Rhythmic Gymnastics Frostvale Trophy

We need a poster for our new annual international rhythmic gymnastics competition "Frostvale Trophy". Dates are December 21 -23, 2019.Picture we would like to use is attached.We would like to see holidays colors in the poster.It should have words "international rhythmic gymnastics", Name of the competition "Frostvale Trophy" and dates.Also we would like for it to say somewhere that it is in Los Angeles, California, USAIt should have information about our club on the bottom of the poster like on the file attached (hosted by Tamrin Gymnastics with logo and address and website info)We also need a flyer that ties into the poster in look and colors with empty space below so we can add directives.We would like end product to be in file format that we can edit next year when the dates change.

Target Market(s)

Rhythmic Gymnastics Clubs

Industry/Entity Type

Gym

Colors

Designer to choose colors to be used in the design.

Requirements
Must have
• Picture we uploaded and all info we requested.
• Bright holiday colors

```html
<!DOCTYPE html>
<html lang="en">
<head>
<meta charset="utf-8">
<title>International Rhythmic Gymnastics Frostvale Trophy</title>
<link href="https://fonts.googleapis.com/css2?family=Open+Sans:wght@400;700;800&family=Cinzel:wght@400;600&family=Roboto+Condensed:wght@400&family=Roboto:wght@400;500&family=Crimson+Text&display=swap" rel="stylesheet">
<style>
  :root {
    --stage: #d9dadc;
    --navy: #1c1a4a;
    --ink: #2a2a3a;
    --sky: #6f92d4;
    --sky-soft: #b9cdec;
    --sun: #f6ea2a;
    --sun-soft: #fbf4a8;
    --glow: #ffffff;
    --magenta: #9b2f8c;
    --teal: #2aa6c4;
    --violet: #5a2f7c;
  }
  html, body {
    margin: 0;
    width: 1200px;
    height: 1200px;
    overflow: hidden;
    background: var(--stage);
  }
  .poster {
    position: absolute;
    left: 163px;
    top: 35px;
    width: 873px;
    height: 1130px;
    overflow: hidden;
    background:
      radial-gradient(ellipse 46% 38% at 50% 52%, var(--glow) 0%, rgba(255,255,255,0.7) 40%, rgba(255,255,255,0) 100%),
      linear-gradient(90deg, var(--sky) 0%, var(--sky-soft) 30%, #eef1ec 50%, var(--sun-soft) 70%, var(--sun) 100%);
    font-family: "Open Sans", sans-serif;
  }
  .poster__rays {
    position: absolute;
    inset: 0;
  }
  .poster__floor {
    position: absolute;
    left: 0; right: 0; bottom: 0;
    height: 260px;
    background: linear-gradient(180deg, rgba(255,255,255,0) 0%, rgba(255,255,255,0.92) 45%, #fff 100%);
  }
  .poster__photo {
    position: absolute;
    left: 100px;
    top: 270px;
    width: 650px;
    height: 640px;
    border-radius: 40%;
    background: radial-gradient(ellipse at 62% 62%, rgba(198,160,122,0.75) 0%, rgba(120,80,150,0.45) 35%, rgba(60,80,170,0.18) 60%, rgba(255,255,255,0) 75%);
  }
  .title { position: absolute; left: 0; width: 100%; text-align: center; margin: 0; }
  .title--kicker {
    top: 58px;
    left: 8px;
    font-weight: 400;
    font-size: 34px;
    letter-spacing: 23px;
    color: var(--navy);
  }
  .title--rhythmic {
    top: 96px;
    left: 22px;
    font-weight: 800;
    font-size: 72px;
    letter-spacing: 8px;
    color: var(--navy);
  }
  .title--main {
    top: 168px;
    left: 26px;
    font-weight: 800;
    font-size: 118px;
    letter-spacing: -3px;
    line-height: 1.1;
    background: linear-gradient(180deg, var(--navy) 0%, var(--teal) 28%, #8fd6e6 42%, var(--violet) 62%, var(--navy) 100%);
    -webkit-background-clip: text;
    background-clip: text;
    color: transparent;
    -webkit-text-stroke: 3px #fff;
    filter: drop-shadow(2px 4px 4px rgba(20,20,60,0.45));
  }
  .event {
    position: absolute;
    left: 260px;
    width: 390px;
    text-align: center;
    color: var(--navy);
    margin: 0;
  }
  .event__name {
    top: 326px;
    font-family: "Cinzel", serif;
    font-weight: 400;
    font-size: 50px;
    line-height: 64px;
  }
  .event__dates {
    top: 452px;
    font-family: "Roboto Condensed", sans-serif;
    font-size: 30px;
    line-height: 36px;
    color: var(--ink);
  }
  .host {
    position: absolute;
    left: 55px;
    top: 1016px;
    width: 300px;
  }
  .host__label {
    margin: 0 0 8px 52px;
    font-family: "Roboto", sans-serif;
    font-weight: 500;
    font-size: 12px;
    letter-spacing: 3px;
    color: var(--ink);
  }
  .host__brand {
    display: flex;
    align-items: center;
    gap: 12px;
    font-family: "Roboto Condensed", sans-serif;
    font-size: 30px;
    color: var(--navy);
  }
  .host__dot {
    width: 34px; height: 34px;
    border-radius: 50%;
    background: var(--navy);
    order: 2;
  }
  .venue {
    position: absolute;
    right: 62px;
    top: 1022px;
    text-align: center;
  }
  .venue__place {
    margin: 0;
    font-family: "Roboto", sans-serif;
    font-size: 21px;
    letter-spacing: 1px;
    color: var(--magenta);
  }
  .venue__web {
    margin: 10px 0 0;
    font-family: "Crimson Text", serif;
    font-size: 24px;
    letter-spacing: 5px;
    color: var(--ink);
  }
</style>
</head>
<body>
  <main class="poster">
    <svg class="poster__rays" viewBox="0 0 873 1130" aria-hidden="true">
      <g fill="#fff" opacity="0.28">
        <polygon points="440,560 0,180 0,260"/>
        <polygon points="440,560 0,420 0,480"/>
        <polygon points="440,560 180,0 260,0"/>
        <polygon points="440,560 560,0 640,0"/>
        <polygon points="440,560 873,140 873,220"/>
        <polygon points="440,560 873,440 873,500"/>
        <polygon points="440,560 873,720 873,800"/>
        <polygon points="440,560 0,700 0,760"/>
      </g>
      <g fill="#fff" opacity="0.3">
        <circle cx="80" cy="175" r="45"/>
        <circle cx="90" cy="655" r="75"/>
        <circle cx="720" cy="440" r="85"/>
        <circle cx="800" cy="320" r="35"/>
        <circle cx="700" cy="650" r="60"/>
        <circle cx="330" cy="80" r="60"/>
      </g>
    </svg>
    <div class="poster__photo" role="img" aria-label="Photo of a rhythmic gymnast in a jewelled leotard in a deep lunge, one arm raised swirling a blue and purple ribbon"></div>
    <div class="poster__floor"></div>

    <p class="title title--kicker">INTERNATIONAL</p>
    <h1 class="title title--rhythmic">RHYTHMIC</h1>
    <p class="title title--main">GYMNASTICS</p>

    <h2 class="event event__name">FROSTVALE<br>TROPHY</h2>
    <p class="event event__dates">DECEMBER<br>21 -23, 2019</p>

    <footer>
      <div class="host">
        <p class="host__label">HOSTED BY</p>
        <div class="host__brand"><span class="host__dot"></span><span>Tamrin Gymnastics</span></div>
      </div>
      <div class="venue">
        <p class="venue__place">Los Angeles, California, USA</p>
        <p class="venue__web">www.Tamringymnastics.com</p>
      </div>
    </footer>
  </main>
</body>
</html>
```